Robotic startup business cards

We are looking for a design for a set of business cards which reflect the spirit and humor of Vortalo Robotics. We want to present ourselves as sleek, professional, but laid-back consulting company.

We primarily focus on developing robotic arms software. This software controls robots and does things like grab items, pick objects up, move them, etc.

We want to allow you maximum design creativity, but do ask that you consider our existing style guidelines (see attached files) in order to make our brand cohesive.

Target Market(s)

Startups and Mid-size robotic companies

Industry/Entity Type

Business

Contact Information for Business Card

Miro Halvensky, PhD
Roboticist | Vortalo Consulting | 318.570.9164

Font styles to use
Other font styles liked:
• Source code pro

Requirements
Must have
• robots or robotic arms
• similar color scheme that works with existing brand guidelines
Nice to have
• please consider our existing style guidelines (see attached files) in order to make our brand cohesive.
• minimalism style is generally nice.
Should not have
• An old, boring, or corporate feel. Too much text.

```html
<!DOCTYPE html>
<html lang="en">
<head>
<meta charset="utf-8">
<title>Vortalo Robotics — Business Cards</title>
<link rel="stylesheet" href="https://fonts.googleapis.com/css2?family=Source+Code+Pro:wght@300;400;700&display=swap">
<style>
  :root {
    --bg: #d2d7d7;
    --card: #0c0c0c;
    --ink: #e9ecea;
    --ink-soft: #cfd3d1;
    --green: #22a35c;
    --ghost: #1c1c1c;
  }
  * { box-sizing: border-box; margin: 0; padding: 0; }
  html, body {
    width: 1200px;
    height: 864px;
    overflow: hidden;
    background: var(--bg);
    font-family: "Source Code Pro", monospace;
  }
  .sheet {
    position: relative;
    width: 1200px;
    height: 864px;
    display: flex;
    align-items: center;
    justify-content: center;
    gap: 60px;
  }
  .card {
    position: relative;
    width: 510px;
    height: 292px;
    background: var(--card);
    border-radius: 3px;
    overflow: hidden;
  }

  /* Front */
  .card-front { padding: 40px 44px; }
  .brand {
    display: flex;
    align-items: center;
    gap: 14px;
  }
  .brand-mark {
    width: 26px;
    height: 26px;
    background: var(--green);
  }
  .brand-name {
    color: var(--ink);
    font-weight: 300;
    font-size: 30px;
    letter-spacing: 6px;
  }
  .contact {
    position: absolute;
    left: 44px;
    right: 44px;
    bottom: 38px;
    color: var(--ink);
  }
  .person-name {
    font-weight: 700;
    font-size: 17px;
  }
  .person-role {
    font-weight: 300;
    font-size: 17px;
    color: var(--ink-soft);
    margin-top: 4px;
  }
  .divider {
    height: 3px;
    width: 100%;
    background: var(--green);
    margin: 14px 0 12px;
  }
  .company, .phone {
    font-weight: 300;
    font-size: 17px;
    color: var(--ink-soft);
    line-height: 1.45;
  }

  /* Back */
  .card-back {
    display: flex;
    align-items: center;
    justify-content: center;
  }
  .ghost-name {
    color: var(--ghost);
    font-weight: 700;
    font-size: 70px;
    letter-spacing: 6px;
  }
</style>
</head>
<body>
  <main class="sheet">
    <section class="card card-front" aria-label="Business card front">
      <div class="brand">
        <span class="brand-mark" aria-hidden="true"></span>
        <span class="brand-name">VORTALO</span>
      </div>
      <div class="contact">
        <p class="person-name">Miro Halvensky, PhD</p>
        <p class="person-role">Roboticist</p>
        <div class="divider" aria-hidden="true"></div>
        <p class="company">Vortalo Consulting</p>
        <p class="phone">318.570.9164</p>
      </div>
    </section>

    <section class="card card-back" aria-label="Business card back">
      <span class="ghost-name">VORTALO</span>
    </section>
  </main>
</body>
</html>
```